Create a memorable Web Design for real estate branding

we are a Minnepolis brokerage and boutique housing specialist with over 27 years of experience in the Global furnished housing industry, servicing the Greater Los Angeles area. Specializing in “warm environments” we offer a customized approach to satisfying our guests and client’s needs by offering a wide array of options in highly desirable areas. Additionally, Lanterly Homes Collective offers assistance and expertise to home buyers, sellers and investors.

Industry/Entity Type

Real Estate

Number of Pages Required

1 page

Font styles to use
Serif
Sans Serif
Decorative

```html
<!DOCTYPE html>
<html lang="en">
<head>
<meta charset="utf-8">
<title>Lanterly Homes — Boutique Housing</title>
<link href="https://fonts.googleapis.com/css2?family=Cinzel:wght@400;700&family=Roboto:wght@300;400;500;700&display=swap" rel="stylesheet">
<style>
:root{
  --green:#7cc242;
  --green-dark:#5fa12c;
  --teal:#1fa88f;
  --teal-dark:#138873;
  --ink:#333;
  --muted:#777;
  --line:#e4e4e4;
  --dark:#1b2025;
  --footer:#2a2a2a;
  --footer-bottom:#1d1d1d;
  --white:#fff;
}
*{box-sizing:border-box;margin:0;padding:0}
html,body{width:1200px;height:3750px;overflow:hidden}
body{position:relative;background:var(--white);font-family:'Roboto',Arial,sans-serif;color:var(--ink)}
.abs{position:absolute}

/* header */
.site-header{left:0;top:0;width:1200px;height:100px;border-top:4px solid var(--teal);background:var(--white)}
.brand{left:100px;top:26px;font-family:'Cinzel',Georgia,serif;font-weight:700;font-size:30px;color:var(--green)}
.nav{right:100px;top:42px;display:flex;gap:42px;font-size:14px;color:#666;list-style:none}
.nav li.active{color:var(--green)}

/* hero */
.hero{left:0;top:100px;width:1200px;height:535px;background:linear-gradient(180deg,#9cc6ea 0%,#c9def0 35%,#b9b0a2 55%,#7fa650 78%,#4f7d2c 100%)}
.hero-tag{left:600px;top:362px;width:500px;height:138px;background:rgba(124,194,66,.85);display:flex;align-items:center;justify-content:center;text-align:center;color:var(--white);font-family:'Cinzel',Georgia,serif;font-size:38px;line-height:1.1}

/* category tabs */
.tabs{left:100px;top:555px;width:1000px;height:135px;background:var(--white);box-shadow:0 6px 18px rgba(0,0,0,.12);display:flex}
.tab{flex:1;display:flex;flex-direction:column;align-items:center;justify-content:flex-start;padding-top:38px;font-size:16px;color:#555;gap:14px}
.tab svg{width:26px;height:26px}
.tab.active{color:var(--green);border-top:4px solid var(--green);padding-top:30px}

/* welcome */
.section-title{font-family:'Cinzel',Georgia,serif;font-size:30px;color:#222;text-align:center;letter-spacing:1px}
.section-title span{color:var(--green)}
.welcome-title{left:0;top:738px;width:1200px}
.welcome-sub{left:0;top:782px;width:1200px;text-align:center;font-size:16px;color:#444}
.welcome-text{left:240px;top:814px;width:720px;text-align:center;font-size:12px;line-height:20px;color:var(--muted)}
.feature{width:250px;top:880px;text-align:center}
.feature .photo{width:160px;height:160px;border-radius:50%;margin:0 auto;border:5px solid var(--white);box-shadow:0 2px 10px rgba(0,0,0,.15)}
.feature h3{margin-top:38px;font-size:15px;font-weight:500;color:#222}
.feature p{margin-top:10px;font-size:12px;line-height:19px;color:var(--muted)}

/* service band */
.service-band{left:0;top:1220px;width:1200px;height:230px;background:linear-gradient(110deg,var(--teal) 0%,#2ab59b 50%,var(--teal-dark) 100%);text-align:center;color:var(--white)}
.service-band h2{margin-top:68px;font-family:'Cinzel',Georgia,serif;font-weight:400;font-size:30px}
.service-band p{width:760px;margin:20px auto 0;font-size:14px;line-height:22px;opacity:.9}

/* housing */
.housing-head{left:100px;top:1505px;width:1000px;display:flex;align-items:center;justify-content:space-between}
.housing-head h2{font-family:'Cinzel',Georgia,serif;font-weight:400;font-size:28px;color:#222}
.housing-head h2 span{color:var(--green)}
.view-tools{display:flex;align-items:center;gap:12px;font-size:12px;color:#666}
.view-tools a{text-decoration:underline;margin-left:10px}
.card{width:315px;height:403px;background:var(--white);border:1px solid var(--line);box-shadow:0 2px 6px rgba(0,0,0,.06)}
.card .photo{height:182px}
.card .meta{height:36px;background:#f3f3f3;border-bottom:2px solid var(--teal);display:flex;align-items:center;gap:16px;padding:0 12px;font-size:10px;color:#666}
.card .meta i{display:inline-block;width:10px;height:8px;background:#888;margin-right:4px;vertical-align:middle}
.card h4{margin:18px 20px 0;font-size:14px;font-weight:500;color:#222}
.card .loc{margin:8px 20px 0;font-size:11px;color:#555;display:flex;align-items:center;gap:6px}
.card .desc{margin:12px 20px 0;font-size:11px;line-height:17px;color:var(--muted)}
.card .foot{position:absolute;left:0;bottom:0;width:100%;height:50px;border-top:1px solid var(--line);display:flex;align-items:center;justify-content:space-between;padding:0 20px;font-size:14px;color:#222}
.card .foot .acts{display:flex;gap:14px}

/* testimonials */
.testimonials{left:0;top:2475px;width:1200px;height:345px;background:linear-gradient(135deg,#232a30 0%,var(--dark) 55%,#12161a 100%)}
.testimonials h2{position:absolute;top:52px;width:100%;text-align:center;font-family:'Cinzel',Georgia,serif;font-weight:400;font-size:30px;color:var(--white)}
.testimonials h2 span{color:var(--green)}
.quote{width:333px;text-align:center;top:130px}
.quote .mark{font-family:Georgia,serif;font-size:64px;line-height:40px;color:var(--green)}
.quote p{width:270px;margin:16px auto 0;font-size:12px;line-height:20px;color:#bbb}
.quote .who{margin-top:16px;font-size:14px;color:var(--green);font-weight:500}

/* agents */
.agents-title{left:0;top:2873px;width:1200px}
.agent{width:330px;height:275px;top:2950px;text-align:center}
.agent.highlight{background:#eceef0}
.agent .photo{width:100px;height:100px;border-radius:50%;margin:20px auto 0;border:4px solid var(--white);box-shadow:0 1px 6px rgba(0,0,0,.15)}
.agent h4{margin-top:22px;font-size:16px;font-weight:500;color:#222}
.agent .role{margin-top:6px;font-size:12px;color:#666}
.agent p{width:260px;margin:12px auto 0;font-size:12px;line-height:20px;color:#666}
.agent .social{margin-top:14px;display:flex;justify-content:center;gap:14px}
.agent .social span{width:10px;height:10px;border-radius:50%;background:#444}

/* newsletter */
.newsletter{left:0;top:3305px;width:1200px;height:107px;background:linear-gradient(90deg,var(--green-dark),var(--green) 50%,var(--green-dark))}
.newsletter h3{position:absolute;left:163px;top:38px;font-family:'Cinzel',Georgia,serif;font-weight:400;font-size:24px;color:var(--white);letter-spacing:1px}
.newsletter .field{position:absolute;left:612px;top:33px;width:360px;height:44px;background:rgba(255,255,255,.25);border:1px solid rgba(255,255,255,.5);font-size:12px;color:#f2f2f2;padding:14px 12px}
.newsletter .go{position:absolute;left:982px;top:33px;width:50px;height:44px;background:var(--teal);color:var(--white);font-size:14px;display:flex;align-items:center;justify-content:center}

/* footer */
.site-footer{left:0;top:3412px;width:1200px;height:276px;background:var(--footer);color:#ccc}
.foot-col h5{font-size:15px;font-weight:500;color:var(--white);margin-bottom:16px}
.foot-col ul{list-style:none;font-size:12px;line-height:26px;color:#ccc}
.post{display:flex;gap:14px;margin-bottom:24px}
.post .thumb{width:72px;height:52px;flex:none}
.post p{font-size:12px;line-height:18px;color:#ddd;width:190px}
.post p b{display:block;font-weight:400;color:var(--white);margin-top:3px}
.footer-bottom{left:0;top:3688px;width:1200px;height:62px;background:var(--footer-bottom);font-size:11px;color:#aaa;display:flex;align-items:center;justify-content:space-between;padding:0 98px}
</style>
</head>
<body>

<header class="abs site-header">
  <div class="abs brand">Lanterly Homes</div>
  <ul class="abs nav">
    <li class="active">Home</li><li>About us</li><li>Services</li><li>Properties</li><li>Our Team</li><li>Blog</li><li>Contact us</li>
  </ul>
</header>

<section class="abs hero" role="img" aria-label="Photo of a large suburban family house with a green lawn, hedges and trees under a blue sky"></section>
<div class="abs hero-tag">Specializing in<br>“warm environments”</div>

<nav class="abs tabs">
  <div class="tab active"><svg viewBox="0 0 26 26"><path d="M4 10h18l-2 11H6z" fill="#7cc242"/><path d="M9 10a4 4 0 0 1 8 0" fill="none" stroke="#7cc242" stroke-width="2"/></svg>Buy</div>
  <div class="tab"><svg viewBox="0 0 26 26"><circle cx="9" cy="9" r="5" fill="none" stroke="#666" stroke-width="2.5"/><path d="M12 12l9 9M17 17l2-2" stroke="#666" stroke-width="2.5"/></svg>Rent</div>
  <div class="tab"><svg viewBox="0 0 26 26"><rect x="3" y="11" width="20" height="7" fill="#666"/><rect x="3" y="7" width="3" height="14" fill="#666"/><rect x="7" y="8" width="6" height="3" fill="#666"/></svg>Hostels</div>
  <div class="tab"><svg viewBox="0 0 26 26"><circle cx="13" cy="13" r="10" fill="#666"/><path d="M9 13h8M13 9v8" stroke="#fff" stroke-width="2"/></svg>Sale</div>
  <div class="tab"><svg viewBox="0 0 26 26"><path d="M3 14l10-8 10 4-8 3-3 8z" fill="#666"/></svg>Property</div>
  <div class="tab"><svg viewBox="0 0 26 26"><path d="M3 13l10-9 10 9h-3v9h-5v-6h-4v6H6v-9z" fill="#666"/></svg>Home</div>
  <div class="tab"><svg viewBox="0 0 26 26"><path d="M5 4h10l-2 6h-8z" fill="#666"/><path d="M14 14l7 7M18 13l3 3" stroke="#666" stroke-width="2.5"/></svg>Projects</div>
  <div class="tab"><svg viewBox="0 0 26 26"><path d="M2 14c4-6 8-6 11-3 3-3 7-3 11 3l-4 4-7-3-7 3z" fill="#666"/></svg>Dealers</div>
</nav>

<h2 class="abs section-title welcome-title">Welcome to <span>Lanterly Homes</span></h2>
<p class="abs welcome-sub">We Are Doing &nbsp;Real estate</p>
<p class="abs welcome-text">It is a long established fact that a reader will be distracted by the readable content of a page when looking at its layout. The point of using Lorem Ipsum is that it has a more-or-less normal distribution of letters, as opposed to using Content here, content here</p>

<div class="abs feature" style="left:80px"><div class="photo" role="img" aria-label="Illustration of a family standing on a green globe with trees" style="background:radial-gradient(circle,#a9d66a,#4c8f2f)"></div><h3>Search From Anywhere</h3><p>There are many variations of passages of Lorem Ipsum available, but the majority have suffered alteration some</p></div>
<div class="abs feature" style="left:340px"><div class="photo" role="img" aria-label="Photo of a smiling couple outdoors" style="background:radial-gradient(circle,#e3c9ad,#8aa0b6)"></div><h3>Search From Anywhere</h3><p>There are many variations of passages of Lorem Ipsum available, but the majority have suffered alteration some</p></div>
<div class="abs feature" style="left:602px"><div class="photo" role="img" aria-label="Photo of a modern house at dusk" style="background:radial-gradient(circle,#f1d2a8,#6d7fa6)"></div><h3>Search From Anywhere</h3><p>There are many variations of passages of Lorem Ipsum available, but the majority have suffered alteration some</p></div>
<div class="abs feature" style="left:865px"><div class="photo" role="img" aria-label="Photo of a hand holding a small model house" style="background:radial-gradient(circle,#c8d3e2,#2c3e58)"></div><h3>Search From Anywhere</h3><p>There are many variations of passages of Lorem Ipsum available, but the majority have suffered alteration some</p></div>

<section class="abs service-band">
  <h2>We are Always There At your Services</h2>
  <p>Sed ut perspiciatis unde omnis iste natus error sit voluptatem accusantium doloremque laudantium, totam aperiam, eaque ipsa quae ab illo inventore veritatis et quasi architecto beatae vitae dicta sunt explicabo.</p>
</section>

<div class="abs housing-head">
  <h2>Boutique <span>Housing</span></h2>
  <div class="view-tools">
    <svg width="16" height="14" viewBox="0 0 16 14"><rect width="7" height="6" fill="#555"/><rect x="9" width="7" height="6" fill="#555"/><rect y="8" width="7" height="6" fill="#555"/><rect x="9" y="8" width="7" height="6" fill="#555"/></svg>
    <svg width="16" height="14" viewBox="0 0 16 14"><rect width="4" height="6" fill="#555"/><rect x="6" width="4" height="6" fill="#555"/><rect x="12" width="4" height="6" fill="#555"/><rect y="8" width="4" height="6" fill="#555"/><rect x="6" y="8" width="4" height="6" fill="#555"/><rect x="12" y="8" width="4" height="6" fill="#555"/></svg>
    <svg width="16" height="14" viewBox="0 0 16 14"><rect width="3" height="3" fill="#555"/><rect x="5" width="11" height="3" fill="#555"/><rect y="5.5" width="3" height="3" fill="#555"/><rect x="5" y="5.5" width="11" height="3" fill="#555"/><rect y="11" width="3" height="3" fill="#555"/><rect x="5" y="11" width="11" height="3" fill="#555"/></svg>
    <a>View More</a>
  </div>
</div>

<article class="abs card" style="left:100px;top:1572px"><div class="photo" role="img" aria-label="Photo of a two-storey family home with a front lawn" style="background:linear-gradient(180deg,#7fb0dc,#b9a58a 55%,#5f8a3a)"></div><div class="meta"><span><i></i>10000 Acres</span><span><i></i>3 Bedrooms</span><span><i></i>3 Bathrooms</span></div><h4>HOME FOR A FAMILY</h4><div class="loc"><svg width="8" height="11" viewBox="0 0 8 11"><path d="M4 0a4 4 0 0 1 4 4c0 3-4 7-4 7S0 7 0 4a4 4 0 0 1 4-4z" fill="#444"/></svg>BOSTON, USA</div><p class="desc">Nemo enim ipsam voluptatem quia to voluptas sit aspernatur odit aut fugit, sed consequuntur</p><div class="foot"><span>$ 1,000,008</span><span class="acts"><svg width="12" height="12" viewBox="0 0 12 12"><circle cx="9" cy="2.5" r="2" fill="#333"/><circle cx="3" cy="6" r="2" fill="#333"/><circle cx="9" cy="9.5" r="2" fill="#333"/><path d="M9 2.5L3 6l6 3.5" stroke="#333" fill="none"/></svg><svg width="13" height="12" viewBox="0 0 13 12"><path d="M6.5 .7l1.8 3.7 4 .5-3 2.8.8 4-3.6-2-3.6 2 .8-4-3-2.8 4-.5z" fill="none" stroke="#333"/></svg></span></div></article>
<article class="abs card" style="left:442px;top:1572px"><div class="photo" role="img" aria-label="Photo of a wooden deck and lit house at dusk" style="background:linear-gradient(180deg,#4a3a3a,#a0684a 55%,#6b4a36)"></div><div class="meta"><span><i></i>10000 Acres</span><span><i></i>3 Bedrooms</span><span><i></i>3 Bathrooms</span></div><h4>HOME FOR A FAMILY</h4><div class="loc"><svg width="8" height="11" viewBox="0 0 8 11"><path d="M4 0a4 4 0 0 1 4 4c0 3-4 7-4 7S0 7 0 4a4 4 0 0 1 4-4z" fill="#444"/></svg>BOSTON, USA</div><p class="desc">Nemo enim ipsam voluptatem quia to voluptas sit aspernatur odit aut fugit, sed consequuntur</p><div class="foot"><span>$ 1,000,008</span><span class="acts"><svg width="12" height="12" viewBox="0 0 12 12"><circle cx="9" cy="2.5" r="2" fill="#333"/><circle cx="3" cy="6" r="2" fill="#333"/><circle cx="9" cy="9.5" r="2" fill="#333"/><path d="M9 2.5L3 6l6 3.5" stroke="#333" fill="none"/></svg><svg width="13" height="12" viewBox="0 0 13 12"><path d="M6.5 .7l1.8 3.7 4 .5-3 2.8.8 4-3.6-2-3.6 2 .8-4-3-2.8 4-.5z" fill="none" stroke="#333"/></svg></span></div></article>
<article class="abs card" style="left:785px;top:1572px"><div class="photo" role="img" aria-label="Photo of a white colonial house with a green lawn" style="background:linear-gradient(180deg,#8cc0e6,#dfe3e6 50%,#5c9a3a)"></div><div class="meta"><span><i></i>10000 Acres</span><span><i></i>3 Bedrooms</span><span><i></i>3 Bathrooms</span></div><h4>HOME FOR A FAMILY</h4><div class="loc"><svg width="8" height="11" viewBox="0 0 8 11"><path d="M4 0a4 4 0 0 1 4 4c0 3-4 7-4 7S0 7 0 4a4 4 0 0 1 4-4z" fill="#444"/></svg>BOSTON, USA</div><p class="desc">Nemo enim ipsam voluptatem quia to voluptas sit aspernatur odit aut fugit, sed consequuntur</p><div class="foot"><span>$ 1,000,008</span><span class="acts"><svg width="12" height="12" viewBox="0 0 12 12"><circle cx="9" cy="2.5" r="2" fill="#333"/><circle cx="3" cy="6" r="2" fill="#333"/><circle cx="9" cy="9.5" r="2" fill="#333"/><path d="M9 2.5L3 6l6 3.5" stroke="#333" fill="none"/></svg><svg width="13" height="12" viewBox="0 0 13 12"><path d="M6.5 .7l1.8 3.7 4 .5-3 2.8.8 4-3.6-2-3.6 2 .8-4-3-2.8 4-.5z" fill="none" stroke="#333"/></svg></span></div></article>
<article class="abs card" style="left:100px;top:2010px"><div class="photo" role="img" aria-label="Photo of a brick house lit up at twilight" style="background:linear-gradient(180deg,#2d3f6b,#b0764a 60%,#3f5a2a)"></div><div class="meta"><span><i></i>10000 Acres</span><span><i></i>3 Bedrooms</span><span><i></i>3 Bathrooms</span></div><h4>HOME FOR A FAMILY</h4><div class="loc"><svg width="8" height="11" viewBox="0 0 8 11"><path d="M4 0a4 4 0 0 1 4 4c0 3-4 7-4 7S0 7 0 4a4 4 0 0 1 4-4z" fill="#444"/></svg>BOSTON, USA</div><p class="desc">Nemo enim ipsam voluptatem quia to voluptas sit aspernatur odit aut fugit, sed consequuntur</p><div class="foot"><span>$ 1,000,008</span><span class="acts"><svg width="12" height="12" viewBox="0 0 12 12"><circle cx="9" cy="2.5" r="2" fill="#333"/><circle cx="3" cy="6" r="2" fill="#333"/><circle cx="9" cy="9.5" r="2" fill="#333"/><path d="M9 2.5L3 6l6 3.5" stroke="#333" fill="none"/></svg><svg width="13" height="12" viewBox="0 0 13 12"><path d="M6.5 .7l1.8 3.7 4 .5-3 2.8.8 4-3.6-2-3.6 2 .8-4-3-2.8 4-.5z" fill="none" stroke="#333"/></svg></span></div></article>
<article class="abs card" style="left:442px;top:2010px"><div class="photo" role="img" aria-label="Photo of a blue two-storey house with a porch" style="background:linear-gradient(180deg,#7ab6e8,#3e6aa0 50%,#6f9a48)"></div><div class="meta"><span><i></i>10000 Acres</span><span><i></i>3 Bedrooms</span><span><i></i>3 Bathrooms</span></div><h4>HOME FOR A FAMILY</h4><div class="loc"><svg width="8" height="11" viewBox="0 0 8 11"><path d="M4 0a4 4 0 0 1 4 4c0 3-4 7-4 7S0 7 0 4a4 4 0 0 1 4-4z" fill="#444"/></svg>BOSTON, USA</div><p class="desc">Nemo enim ipsam voluptatem quia to voluptas sit aspernatur odit aut fugit, sed consequuntur</p><div class="foot"><span>$ 1,000,008</span><span class="acts"><svg width="12" height="12" viewBox="0 0 12 12"><circle cx="9" cy="2.5" r="2" fill="#333"/><circle cx="3" cy="6" r="2" fill="#333"/><circle cx="9" cy="9.5" r="2" fill="#333"/><path d="M9 2.5L3 6l6 3.5" stroke="#333" fill="none"/></svg><svg width="13" height="12" viewBox="0 0 13 12"><path d="M6.5 .7l1.8 3.7 4 .5-3 2.8.8 4-3.6-2-3.6 2 .8-4-3-2.8 4-.5z" fill="none" stroke="#333"/></svg></span></div></article>
<article class="abs card" style="left:785px;top:2010px"><div class="photo" role="img" aria-label="Photo of a modern white house with a garden" style="background:linear-gradient(180deg,#d9dde0,#b8b4aa 55%,#7a8a5c)"></div><div class="meta"><span><i></i>10000 Acres</span><span><i></i>3 Bedrooms</span><span><i></i>3 Bathrooms</span></div><h4>HOME FOR A FAMILY</h4><div class="loc"><svg width="8" height="11" viewBox="0 0 8 11"><path d="M4 0a4 4 0 0 1 4 4c0 3-4 7-4 7S0 7 0 4a4 4 0 0 1 4-4z" fill="#444"/></svg>BOSTON, USA</div><p class="desc">Nemo enim ipsam voluptatem quia to voluptas sit aspernatur odit aut fugit, sed consequuntur</p><div class="foot"><span>$ 1,000,008</span><span class="acts"><svg width="12" height="12" viewBox="0 0 12 12"><circle cx="9" cy="2.5" r="2" fill="#333"/><circle cx="3" cy="6" r="2" fill="#333"/><circle cx="9" cy="9.5" r="2" fill="#333"/><path d="M9 2.5L3 6l6 3.5" stroke="#333" fill="none"/></svg><svg width="13" height="12" viewBox="0 0 13 12"><path d="M6.5 .7l1.8 3.7 4 .5-3 2.8.8 4-3.6-2-3.6 2 .8-4-3-2.8 4-.5z" fill="none" stroke="#333"/></svg></span></div></article>

<section class="abs testimonials">
  <h2>Our Client <span>Testimonial</span></h2>
  <div class="abs quote" style="left:100px"><div class="mark">“</div><p>I must explain to you how all this mistaken idea of denouncing pleasure and praising pain was born and I will give you a complete account of the system, and expound the actual teachings of the explorer of the truth</p><div class="who">- Mara &amp; Owen Pell</div></div>
  <div class="abs quote" style="left:433px"><div class="mark">“</div><p>I must explain to you how all this mistaken idea of denouncing pleasure and praising pain was born and I will give you a complete account of the system, and expound the actual teachings of the explorer of the truth</p><div class="who">- Mara &amp; Owen Pell</div></div>
  <div class="abs quote" style="left:766px"><div class="mark">“</div><p>I must explain to you how all this mistaken idea of denouncing pleasure and praising pain was born and I will give you a complete account of the system, and expound the actual teachings of the explorer of the truth</p><div class="who">- Mara &amp; Owen Pell</div></div>
</section>

<h2 class="abs section-title agents-title">Our <span>Team Agents</span></h2>
<div class="abs agent" style="left:100px"><div class="photo" role="img" aria-label="Portrait photo of a female agent" style="background:radial-gradient(circle,#d9b79a,#6a4a3a)"></div><h4>Elias Varno</h4><div class="role">CEO, Co-Founder</div><p>It is a long established fact that a on the reader will be distracted by the readable content</p><div class="social"><span></span><span></span><span></span></div></div>
<div class="abs agent highlight" style="left:435px"><div class="photo" role="img" aria-label="Portrait photo of a female agent" style="background:radial-gradient(circle,#e6c6a6,#9a6a4a)"></div><h4>Elias Varno</h4><div class="role">CEO, Co-Founder</div><p>It is a long established fact that a on the reader will be distracted by the readable content</p><div class="social"><span></span><span></span><span></span></div></div>
<div class="abs agent" style="left:770px"><div class="photo" role="img" aria-label="Portrait photo of a male agent" style="background:radial-gradient(circle,#d8b89c,#7a6a60)"></div><h4>Elias Varno</h4><div class="role">CEO, Co-Founder</div><p>It is a long established fact that a on the reader will be distracted by the readable content</p><div class="social"><span></span><span></span><span></span></div></div>

<section class="abs newsletter">
  <h3>Subscribe to our Newsletter</h3>
  <div class="field">Enter Your Mail id</div>
  <div class="go">Go</div>
</section>

<footer class="abs site-footer">
  <div class="abs foot-col" style="left:133px;top:44px"><h5>Site Map</h5><ul><li>Home</li><li>About us</li><li>Services</li><li>Properties</li><li>Blog</li></ul></div>
  <div class="abs foot-col" style="left:315px;top:44px"><h5>Latest News Feeds</h5>
    <div class="post"><div class="thumb" role="img" aria-label="Thumbnail photo of a house" style="background:linear-gradient(180deg,#8bb8de,#7a9a5a)"></div><p>There are many variations of passages of Lorem Ipsum available, but majority<b>Read More</b></p></div>
    <div class="post"><div class="thumb" role="img" aria-label="Thumbnail photo of a house at dusk" style="background:linear-gradient(180deg,#2d3f6b,#b0764a)"></div><p>There are many variations of passages of Lorem Ipsum available, but majority<b>Read More</b></p></div>
  </div>
  <div class="abs foot-col" style="left:730px;top:44px"><h5>Recent post</h5>
    <div class="post"><div class="thumb" role="img" aria-label="Thumbnail photo of a house" style="background:linear-gradient(180deg,#7ab6e8,#5a7a9a)"></div><p>There are many variations of passages of Lorem Ipsum available, but majority<b>Read More</b></p></div>
    <div class="post"><div class="thumb" role="img" aria-label="Thumbnail photo of a house" style="background:linear-gradient(180deg,#a9c8e0,#8a7a5a)"></div><p>There are many variations of passages of Lorem Ipsum available, but majority<b>Read More</b></p></div>
  </div>
</footer>
<div class="abs footer-bottom"><span>FAQ &nbsp;/&nbsp; FRIENDS &nbsp;/&nbsp; UPDATES &nbsp;/&nbsp; GALLERY &nbsp;/&nbsp; BOARDS</span><span>Copyrights@2016 Lanterly Homes Collective, All rights reserved</span></div>

</body>
</html>
```